Web Design Project for Communications Agency

The design I need (PSD file) is for an agency offering specialised PR and communications services for customers in the healthcare sector.

OBJECTIVES OF THE WEBSITE:
1. To promote the agency's communication services
2. To position Solène Verbruggen as an industry leader, an expert in healthcare PR and communications by highlighting blogposts and social media.

WHAT I NEED:
1st, I need the design for the Home Page ONLY.
Once approved, I will need the other pages designed as well. (Here is prototype that we've already developed for the Website that will guide you in the design:
http://qoravenlab.com/solenverbruggen/)

VISUAL INSPIRATION
We want to give this Website a "Flat Design" look. Here are some websites for inspiration :
- http://lumbrafolk.com/#!/process
- http://www.quillmarsh.co/
- http://dorvellink.com/

Also, reuse images found on the company's current Website :
http://www.solenverbruggen.com/fr/index.html

HOMEPAGE MAIN ELEMENTS:
1. Main menu : 6 sections
Accueil | Agence | Services | Approche | Publications | Contact

2. Main Call To Action (big dark rectangle in prototype):
Can be slider or just an information bloc.

3. Publications récentes :
The 4 latest blog posts must be features on the homepage (will be linked with the "Publications" section)

4. Dynamic Footer :
Contains a Chirper feed and a Subscribe to our Newsletter feature (revecez nos publications)

OTHER PAGES (to design once Homepage is approved)
- Agence (about us)
- Services (our team)
- Approche (our approach)
- Publications (blog articles)
- Contact (Contact us)

• Please refer to prototype :
http://qoravenlab.com/solenverbruggen/
Must have ALL features present in prototype.

Also, must reuse this picture in the design : http://solenverbruggen.com/static/images/home-big-box.jpg

Finally, you will find attached the company logo.

```html
<!DOCTYPE html>
<html lang="fr">
<head>
<meta charset="utf-8">
<title>Solène Verbruggen — Gestion d'enjeux, affaires publiques</title>
<link rel="stylesheet" href="https://fonts.googleapis.com/css2?family=Oswald:wght@400;600;700&family=Open+Sans:wght@400;600&display=swap">
<style>
  :root {
    --red: #e1404a;
    --red-dark: #c7333c;
    --grey-text: #6f6f6f;
    --grey-soft: #8a8a8a;
    --hero-bg: #ececec;
    --card-bg: #f2f2f2;
    --card-bg-alt: #f8f6f6;
    --footer-bg: #3d3d3d;
    --white: #ffffff;
    --social-blue: #1aa3e8;
  }
  * { box-sizing: border-box; margin: 0; padding: 0; }
  html, body { width: 754px; height: 1200px; overflow: hidden; }
  body { position: relative; background: var(--white); font-family: Arial, Helvetica, sans-serif; }

  .topbar { position: absolute; top: 0; left: 0; width: 754px; height: 5px; background: var(--red); }

  .hero { position: absolute; top: 5px; left: 0; width: 754px; height: 413px;
    background: linear-gradient(160deg, #f6f6f6 0%, var(--hero-bg) 55%, #e2e2e2 100%); overflow: hidden; }
  .hero-curve { position: absolute; inset: 0; }
  .hero-band { position: absolute; top: 418px; left: 0; width: 754px; height: 12px; background: var(--red); }

  .brand { position: absolute; left: 67px; top: 16px; }
  .brand-name { font-family: 'Oswald', sans-serif; font-weight: 400; color: var(--red);
    font-size: 44px; line-height: 44px; letter-spacing: -0.5px; text-transform: lowercase; }
  .brand-rule { width: 30px; height: 2px; background: var(--red); margin: 8px 0 5px; }
  .brand-tag { font-family: 'Oswald', sans-serif; font-size: 14px; line-height: 15px; color: #555; letter-spacing: 0.3px; }
  .brand-tag span { display: block; color: var(--grey-soft); }

  .nav { position: absolute; top: 14px; left: 268px; display: flex; }
  .nav a { display: flex; flex-direction: column; align-items: center; text-decoration: none;
    font-family: 'Oswald', sans-serif; font-weight: 700; font-size: 15px; color: var(--grey-soft);
    padding: 0 6px 4px; }
  .nav a svg { width: 22px; height: 22px; margin-bottom: 2px; fill: none; stroke: #9a9a9a; stroke-width: 1.6; }
  .nav a.is-active { color: var(--red); border-bottom: 3px solid var(--red); }
  .nav a.is-active svg { stroke: var(--red); }

  .hero-title { position: absolute; left: 70px; top: 190px; width: 370px; font-family: 'Oswald', sans-serif;
    font-weight: 700; font-size: 21px; line-height: 31px; color: var(--grey-text); }
  .btn { display: inline-flex; align-items: center; justify-content: center; gap: 6px; background: var(--red);
    color: var(--white); font-family: 'Open Sans', sans-serif; text-decoration: none;
    box-shadow: 2px 2px 0 var(--red-dark); }
  .btn .plus { width: 11px; height: 11px; border: 1px solid var(--white); border-radius: 50%;
    font-size: 9px; line-height: 9px; text-align: center; }
  .hero-cta { position: absolute; left: 67px; top: 291px; width: 132px; height: 31px; font-size: 14px; }
  .hero-visual { position: absolute; left: 486px; top: 178px; width: 200px; height: 210px;
    background: radial-gradient(circle at 45% 40%, #ffffff 0%, #e6e6e6 55%, rgba(225,64,74,0.15) 100%); border-radius: 8px; }

  .section-title { position: absolute; left: 34px; top: 450px; font-family: 'Oswald', sans-serif;
    font-weight: 700; font-size: 24px; color: var(--red); }

  .feature-band { position: absolute; top: 739px; left: 0; width: 754px; height: 283px; background: var(--red); }

  .card { position: absolute; width: 336px; height: 238px; background: var(--card-bg); padding: 11px 13px 0 9px; }
  .card.alt { background: var(--card-bg-alt); height: 237px; }
  .card-photo { float: left; width: 138px; height: 120px; margin: 0 13px 3px 0; }
  .card-title { font-family: 'Oswald', sans-serif; font-weight: 700; font-size: 18px; line-height: 22px; color: #7a7a7a; }
  .card.alt .card-title { color: var(--red); }
  .card-date { text-align: right; font-size: 10.5px; color: var(--red); padding: 2px 0 5px;
    border-bottom: 1px solid #e8c9cb; margin-bottom: 5px; }
  .card-text { font-size: 10px; line-height: 11.3px; color: #777; text-align: justify; }
  .card-btn { position: absolute; right: 13px; bottom: 20px; width: 95px; height: 23px; font-size: 10.5px; }

  .footer { position: absolute; top: 1022px; left: 0; width: 754px; height: 178px; background: var(--footer-bg); }
  .social-name { position: absolute; left: 93px; top: 14px; font-family: 'Open Sans', sans-serif;
    font-weight: 600; font-size: 22px; line-height: 24px; color: var(--white); }
  .tweet { position: absolute; left: 93px; width: 200px; font-family: 'Open Sans', sans-serif;
    font-size: 9.5px; line-height: 10px; color: var(--white); }
  .tweet a { color: var(--red); text-decoration: none; }
  .follow-btn { position: absolute; left: 93px; top: 139px; width: 109px; height: 18px; background: var(--social-blue);
    color: var(--white); font-size: 7.5px; font-weight: bold; display: flex; align-items: center; padding-left: 8px; gap: 6px;
    text-decoration: none; }
  .follow-btn i { width: 8px; height: 8px; background: var(--white); display: block; }
  .subscribe-title { position: absolute; left: 453px; top: 12px; font-family: 'Oswald', sans-serif;
    font-weight: 700; font-size: 18px; line-height: 22px; color: var(--white); }
  .field { position: absolute; left: 453px; width: 194px; height: 24px; background: #f1f1f1;
    font-family: 'Open Sans', sans-serif; font-size: 14px; color: #aaa; padding-left: 7px; display: flex; align-items: center; }
  .subscribe-btn { position: absolute; left: 453px; top: 110px; width: 194px; height: 31px; font-size: 14px; }
  .copyright { position: absolute; left: 454px; top: 159px; font-family: 'Open Sans', sans-serif; font-size: 9px; color: #9a9a9a; }
</style>
</head>
<body>
  <div class="topbar"></div>

  <header class="hero">
    <svg class="hero-curve" viewBox="0 0 754 413" preserveAspectRatio="none" aria-hidden="true">
      <path d="M0 150 C 180 240, 330 300, 400 413 L 0 413 Z" fill="#e6e6e6" opacity="0.6"/>
      <path d="M420 0 C 560 60, 680 40, 754 90 L 754 0 Z" fill="#f8f8f8" opacity="0.8"/>
    </svg>

    <div class="brand">
      <div class="brand-name">solène<br>verbruggen</div>
      <div class="brand-rule"></div>
      <div class="brand-tag">GESTION D'ENJEUX<span>AFFAIRES PUBLIQUES</span></div>
      <div class="brand-rule"></div>
    </div>

    <nav class="nav">
      <a href="#" class="is-active"><svg viewBox="0 0 22 22"><path d="M3 8 L11 4 L19 8 L11 12 Z M3 8 V15 L11 19 V12 M19 8 V15 L11 19"/></svg>Accueil</a>
      <a href="#"><svg viewBox="0 0 22 22"><circle cx="9" cy="9" r="4"/><circle cx="16" cy="16" r="3"/><path d="M9 3 V5 M9 13 V15 M3 9 H5 M13 9 H15"/></svg>Services</a>
      <a href="#"><svg viewBox="0 0 22 22"><rect x="7" y="3" width="10" height="13"/><rect x="4" y="6" width="10" height="13"/><path d="M6 10 H12 M6 13 H12 M6 16 H12"/></svg>Publications</a>
      <a href="#"><svg viewBox="0 0 22 22"><circle cx="11" cy="7" r="4"/><path d="M3 19 C3 13, 19 13, 19 19 Z"/></svg>Agence</a>
      <a href="#"><svg viewBox="0 0 22 22"><path d="M2 9 L20 3 L13 19 L10 12 Z M10 12 L20 3"/></svg>Approche</a>
      <a href="#"><svg viewBox="0 0 22 22"><rect x="3" y="5" width="16" height="12"/><path d="M3 5 L11 12 L19 5"/></svg>Contact</a>
    </nav>

    <h1 class="hero-title">Cabinet-conseil en communications et affaires publiques spécialisé dans le secteur de la santé.</h1>
    <a href="#" class="btn hero-cta">En Savoir plus <span class="plus">+</span></a>
    <div class="hero-visual" role="img" aria-label="Cube blanc en trois dimensions portant une croix rouge sur sa face supérieure"></div>
  </header>
  <div class="hero-band"></div>

  <h2 class="section-title">Publication récentes</h2>

  <div class="feature-band"></div>

  <article class="card" style="left:33px; top:490px;">
    <div class="card-photo" role="img" aria-label="Photo d'une réunion de travail autour d'une table" style="background:linear-gradient(135deg,#b9a58a,#6b5a48 60%,#3d342c);"></div>
    <h3 class="card-title">Titre de la publication</h3>
    <p class="card-date">◷ 23 juillet 2013</p>
    <p class="card-text">Lorem ipsum dolor sit amet, consectetur adipisicing elit, sed do eiusmod tempor incididunt ut labore et dolore magna aliqua. Ut enim ad minim veniam, quis nostrud exercitation ullamco laboris nisi ut aliquip ex ea commodo consequat. Duis aute irure dolor in reprehenderit in voluptate velit esse Duis aute irure dolor in reprehenderit in voluptate velit esse cillum dolore eu fugiat nulla pariatur. Excepteur sint occaecat cupidatat non proident, sunt in culpa qui officia deserunt mollit anim id est laborum.</p>
    <a href="#" class="btn card-btn">Article complet <span class="plus">+</span></a>
  </article>

  <article class="card" style="left:384px; top:490px;">
    <div class="card-photo" role="img" aria-label="Photo d'un homme âgé souriant accompagné d'un soignant" style="background:linear-gradient(135deg,#dfe6ea,#c9c0b4 55%,#8f8a84);"></div>
    <h3 class="card-title">Titre de la publication</h3>
    <p class="card-date">◷ 23 juillet 2013</p>
    <p class="card-text">Lorem ipsum dolor sit amet, consectetur adipisicing elit, sed do eiusmod tempor incididunt ut labore et dolore magna aliqua. Ut enim ad minim veniam, quis nostrud exercitation ullamco laboris nisi ut aliquip ex ea commodo consequat. Duis aute irure dolor in reprehenderit in voluptate velit esse Duis aute irure dolor in reprehenderit in voluptate velit esse cillum dolore eu fugiat nulla pariatur. Excepteur sint occaecat cupidatat non proident, sunt in culpa qui officia deserunt mollit anim id est laborum.</p>
    <a href="#" class="btn card-btn">Article complet <span class="plus">+</span></a>
  </article>

  <article class="card alt" style="left:33px; top:762px;">
    <div class="card-photo" role="img" aria-label="Photo d'une personne parlant dans un porte-voix sur une colline" style="background:linear-gradient(180deg,#2f6fc4,#7fb1e6 55%,#5f9a3a 80%,#3f7a22);"></div>
    <h3 class="card-title">Titre de la publication</h3>
    <p class="card-date">◷ 23 juillet 2013</p>
    <p class="card-text">Lorem ipsum dolor sit amet, consectetur adipisicing elit, sed do eiusmod tempor incididunt ut labore et dolore magna aliqua. Ut enim ad minim veniam, quis nostrud exercitation ullamco laboris nisi ut aliquip ex ea commodo consequat. Duis aute irure dolor in reprehenderit in voluptate velit esse Duis aute irure dolor in reprehenderit in voluptate velit esse cillum dolore eu fugiat nulla pariatur. Excepteur sint occaecat cupidatat non proident, sunt in culpa qui officia deserunt mollit anim id est laborum.</p>
    <a href="#" class="btn card-btn">Article complet <span class="plus">+</span></a>
  </article>

  <article class="card alt" style="left:384px; top:762px;">
    <div class="card-photo" role="img" aria-label="Photo de deux mains qui se tiennent sur fond bleu clair" style="background:linear-gradient(135deg,#a9d4ef,#e8c8b4 55%,#cfe6f5);"></div>
    <h3 class="card-title">Titre de la publication</h3>
    <p class="card-date">◷ 23 juillet 2013</p>
    <p class="card-text">Lorem ipsum dolor sit amet, consectetur adipisicing elit, sed do eiusmod tempor incididunt ut labore et dolore magna aliqua. Ut enim ad minim veniam, quis nostrud exercitation ullamco laboris nisi ut aliquip ex ea commodo consequat. Duis aute irure dolor in reprehenderit in voluptate velit esse Duis aute irure dolor in reprehenderit in voluptate velit esse cillum dolore eu fugiat nulla pariatur. Excepteur sint occaecat cupidatat non proident, sunt in culpa qui officia deserunt mollit anim id est laborum.</p>
    <a href="#" class="btn card-btn">Article complet <span class="plus">+</span></a>
  </article>

  <footer class="footer">
    <div class="social-name">chirper</div>
    <p class="tweet" style="top:53px;">Velit esse eu fugiat nulla pariatur. Excepteur sint occaecat cupidatat non proident. <a href="#">@SoleneVerbruggen #EnjeuSanté</a></p>
    <p class="tweet" style="top:92px;">Velit esse cillum dolore eu fugiat nulla pariatur. Excepteur sint occaecat cupidatat non proident. <a href="#">@SoleneVerbruggen #EnjeuSanté</a></p>
    <a href="#" class="follow-btn"><i></i>Follow us on Chirper</a>

    <h2 class="subscribe-title">Recevez nos publications</h2>
    <div class="field" style="top:41px;">Votre nom</div>
    <div class="field" style="top:75px;">Votre courriel</div>
    <a href="#" class="btn subscribe-btn">Abonnez-vous <span class="plus">+</span></a>
    <p class="copyright">(c) Solène Verbruggen. Tous droits réservés.</p>
  </footer>
</body>
</html>
```